Farrowell Tavern

I am seeking a draft rack card for a client. Please NOTE - I only have FPO low res pix at this point...would send hi res pix if I get the job. The Tavern wants a "warm" feeling to convey the "Hollowmere Ridge comfort food" that it specializes in. It's not vital to use all of the images included, but wanted to offer a choice.

```html
<!DOCTYPE html>
<html lang="en">
<head>
<meta charset="utf-8">
<title>Farrowell Tavern – Rack Cards</title>
<link href="https://fonts.googleapis.com/css2?family=Cabin:ital,wght@0,400;0,600;1,400&display=swap" rel="stylesheet">
<style>
  :root {
    --page: #e6e6e4;
    --paper: #ffffff;
    --wood-dark: #141414;
    --wood-mid: #3a3a3a;
    --tan: #c8b895;
    --tan-band: #bfb29a;
    --ink: #111111;
    --light: #f4f4f2;
  }
  * { margin: 0; padding: 0; box-sizing: border-box; }
  html, body { width: 1200px; height: 1078px; overflow: hidden; }
  body {
    background: var(--page);
    font-family: "Cabin", sans-serif;
    position: relative;
  }
  .rack-card {
    position: absolute;
    top: 98px;
    width: 406px;
    height: 881px;
    overflow: hidden;
    background: linear-gradient(90deg, var(--wood-dark) 0%, var(--wood-mid) 30%, #2a2a2a 55%, var(--wood-mid) 75%, var(--wood-dark) 100%);
  }
  .rack-card--front { left: 127px; }
  .rack-card--back { left: 673px; }

  .header-curve { position: absolute; left: 0; top: 0; width: 406px; }

  .brand {
    position: absolute;
    left: 0; width: 100%;
    text-align: center;
    color: var(--ink);
    font-weight: 600;
    letter-spacing: 2px;
    text-transform: uppercase;
    line-height: 1.05;
  }
  .rack-card--front .brand { top: 120px; font-size: 40px; }
  .rack-card--back .brand { top: 58px; font-size: 34px; }

  .tagline {
    position: absolute;
    top: 464px; left: 0; width: 100%;
    text-align: center;
    color: var(--tan);
    font-size: 21px;
    line-height: 33px;
    text-transform: uppercase;
  }
  .divider {
    position: absolute;
    top: 598px; left: 44px;
    width: 314px; height: 1px;
    background: var(--tan);
  }
  .hours {
    position: absolute;
    top: 626px; left: 0; width: 100%;
    text-align: center;
    color: var(--light);
    font-size: 18px;
    line-height: 27px;
  }
  .hours__title {
    color: var(--tan);
    font-size: 21px;
    text-transform: uppercase;
    line-height: 30px;
  }

  .social {
    position: absolute;
    top: 748px; left: 0; width: 100%;
    display: flex; justify-content: center; gap: 32px;
  }
  .social__dot {
    width: 25px; height: 25px;
    border: 1.5px solid var(--tan);
    border-radius: 50%;
  }

  .contact {
    position: absolute;
    top: 796px; left: 0; width: 100%;
    text-align: center;
    color: var(--light);
    font-size: 16px;
    line-height: 21px;
  }

  .photo {
    position: absolute;
  }
  .photo--hero {
    top: 150px; left: 0; width: 406px; height: 225px;
    background: linear-gradient(180deg, #5d7a3e 0%, #6e7f55 40%, #7b6a4a 70%, #a5542c 100%);
  }
  .photo--soup { top: 383px; left: 0; width: 130px; height: 127px;
    background: radial-gradient(circle at 45% 55%, #f0ede0 0%, #dcd6c2 45%, #8a5a34 80%); }
  .photo--burger { top: 383px; left: 137px; width: 130px; height: 127px;
    background: radial-gradient(circle at 40% 45%, #c98a3e 0%, #8b4a22 40%, #3c4650 85%); }
  .photo--dessert { top: 383px; left: 273px; width: 133px; height: 127px;
    background: radial-gradient(circle at 50% 55%, #f2ead6 0%, #c9b48e 45%, #4a3222 85%); }
  .photo-gap {
    position: absolute; top: 375px; left: 0; width: 406px; height: 141px;
    background: var(--paper);
  }
  .back-wood-top {
    position: absolute; top: 516px; left: 0; width: 406px; height: 1px;
  }

  .credit {
    position: absolute;
    top: 525px; right: 26px;
    color: #cfcfcf;
    font-size: 8px;
    font-style: italic;
  }
  .story {
    position: absolute;
    top: 571px; left: 26px; width: 354px;
    text-align: center;
    color: var(--light);
    font-size: 12.8px;
    line-height: 17.3px;
    letter-spacing: -0.2px;
  }
  .story p + p { margin-top: 17px; }
</style>
</head>
<body>

  <section class="rack-card rack-card--front">
    <svg class="header-curve" viewBox="0 0 406 345" width="406" height="345" aria-hidden="true">
      <path d="M0 0 H406 V275 Q200 360 0 286 Z" fill="var(--tan-band)"/>
      <path d="M0 0 H406 V265 Q200 345 0 276 Z" fill="var(--paper)"/>
    </svg>
    <h1 class="brand">Farrowell<br>Tavern</h1>

    <p class="tagline">Serving mountain comfort food<br>Local draft beers<br>&amp; handcrafted cocktails</p>
    <div class="divider"></div>
    <div class="hours">
      <p class="hours__title">Open for dinner</p>
      <p>Thursday-Monday</p>
      <p>Sunday Brunch 11 a.m.-3 p.m.</p>
    </div>

    <div class="social">
      <span class="social__dot"></span>
      <span class="social__dot"></span>
    </div>

    <address class="contact" style="font-style:normal">
      212 Mill Street Ashbrook, NY<br>
      555 014-2290<br>
      Farrowelltavern.com
    </address>
  </section>

  <section class="rack-card rack-card--back">
    <div class="photo-gap"></div>
    <div class="photo photo--hero" role="img" aria-label="Fresh local produce on a table beside the stream with a footbridge behind"></div>
    <svg class="header-curve" viewBox="0 0 406 215" width="406" height="215" aria-hidden="true">
      <path d="M0 0 H406 V150 Q210 260 0 168 Z" fill="var(--tan-band)"/>
      <path d="M0 0 H406 V142 Q210 248 0 160 Z" fill="var(--paper)"/>
    </svg>
    <h2 class="brand">Farrowell<br>Tavern</h2>

    <div class="photo photo--soup" role="img" aria-label="Bowl of creamy soup"></div>
    <div class="photo photo--burger" role="img" aria-label="Burger with fries"></div>
    <div class="photo photo--dessert" role="img" aria-label="Slice of blueberry cheesecake"></div>

    <p class="credit">Photos by Lena Marsh</p>

    <div class="story">
      <p>Farrowell Tavern - a local food establishment built over the Farrowell stream. The tavern is a place for respite after skiing, fishing, hiking or a hard day's work. It's a place for a nice hearty meal, a handcrafted cocktail and homemade dessert.</p>
      <p>Serving handcrafted food and beverages, Farrowell Tavern is a modern nod to old world inns, taverns and mountain lodges; a stopping place for weary travelers, a place for folks to recharge, warm up and fill their bellies with satisfying food and drink.</p>
    </div>

    <div class="social">
      <span class="social__dot"></span>
      <span class="social__dot"></span>
    </div>

    <address class="contact" style="font-style:normal">
      212 Mill Street Ashbrook, NY<br>
      555 014-2290<br>
      Farrowelltavern.com
    </address>
  </section>

</body>
</html>
```